Premium Personal Brand — Facebook Banner (Used Across All Platforms)

Update — Additional Color Direction
In addition to the dark charcoal/slate direction already described, I'm also interested in seeing variants with:
Dark navy blue — Deep, authoritative, intelligence-community feel. Same textured/matte treatment, not flat or bright.
Warm charcoal with steel blue accent — Keep the dark base but introduce a subtle steel blue gradient, accent line, or tonal shift. Sophisticated, modern, adds dimension without adding color noise.
Both should maintain the same premium, restrained, architectural feel described in the original brief. No bright blues, no corporate PowerPoint energy — think midnight, think depth, think weight.
Everything else in the brief remains the same.
I am building a premium personal brand as an executive advisor to founders ($5M+ revenue).
This contest is Facebook-banner–focused, but the design must represent a visual system that will be reused across:
- LinkedIn
- YouTube
I- nstagram
- X (Twitter)
- Website hero sections and other brand touchpoints
Think of the Facebook banner as the primary expression of the brand — not a one-off graphic.
This project is about discovering a high-end visual style and brand feel, not decoration.
What to design
Please submit one cohesive visual system, shown primarily as:
- Facebook banner (primary focus)
The same design language should clearly translate to all platforms listed above.
Designers are responsible for using the current recommended dimensions for each platform.
Quick clarification on background direction:
Backgrounds should have depth and texture, not flat color fields. Avoid pure white, light grey, or solid black backgrounds. Think matte, architectural materials — stone, graphite, concrete, steel — not blank canvases. Subtle tonal variation is encouraged. Obvious gradients or decorative patterns are not.
Text to use
Primary Headline:
- Your Business Is Too Valuable To Be Run On Hope.
Subheadline:
- You didn’t build a business to become its prisoner.
Name:
Paul Whitaker
The headline should be the dominant visual element.
Logo note (important)
My personal logo is currently being finalized.
For this contest:
- Use a simple “PW” monogram placeholder
- Clean, bold, geometric sans-serif
- Do not design a logo
- The winning design must allow an easy logo swap later.
Headshot note (important)
- Please do not include a headshot in the banner design.
- Most platforms display a circular profile image separately.
- The banner should stand on its own using typography, layout, and tone only.
- Design the banner assuming the profile photo will sit nearby, not inside the banner.
Style direction
The design should feel:
- Premium
- Calm
- Confident
- Restrained
- High-trust
- Dark, neutral backgrounds are preferred.
- Fewer elements are better than more.
Think:
- Owner-level advisor
- Private equity / boardroom tone
- Industrial, Modern, Minimalist, Elite, Architectural, not decorative
What to avoid
Please do not submit designs that feel:
- Promotional, hype-driven, or salesy
- Like a coach, guru, or agency
- Bright, colorful, or gradient-heavy
- Busy or over-designed
- Based on stock photos
- No motivational speaker energy.
Reaction test
- If someone sees this banner on Facebook (or later on LinkedIn, YouTube, etc.), the reaction should be:
“That person is serious. I’d trust them with important decisions.”
Final note
- I am not looking for many variations.
- I am looking for one strong visual direction you believe in.
Simple beats clever.
- Restraint beats decoration.

```html
<!DOCTYPE html>
<html lang="en">
<head>
<meta charset="utf-8">
<title>Paul Whitaker — Banner</title>
<link rel="stylesheet" href="https://fonts.googleapis.com/css2?family=Montserrat:wght@300;600;700&display=swap">
<style>
  :root {
    --ink: #ffffff;
    --graphite-deep: #050505;
    --graphite-mid: #2a2a2c;
    --graphite-light: #4a4b4e;
    --ice-highlight: #8c8f94;
  }
  html, body {
    margin: 0;
    padding: 0;
    width: 1200px;
    height: 457px;
    overflow: hidden;
    background: var(--graphite-deep);
  }
  .banner {
    position: relative;
    width: 1200px;
    height: 457px;
    overflow: hidden;
    font-family: "Montserrat", sans-serif;
    color: var(--ink);
  }
  .banner__texture {
    position: absolute;
    inset: 0;
    background:
      radial-gradient(ellipse 260px 200px at 1010px 170px, rgba(140,143,148,0.55), transparent 70%),
      radial-gradient(ellipse 200px 160px at 820px 300px, rgba(110,112,116,0.35), transparent 70%),
      radial-gradient(ellipse 600px 380px at 380px 220px, var(--graphite-light), transparent 80%),
      linear-gradient(90deg, var(--graphite-mid) 0%, #222224 55%, #161617 80%, var(--graphite-deep) 100%);
  }
  .headline {
    position: absolute;
    left: 63px;
    top: 44px;
    margin: 0;
    font-weight: 700;
    font-size: 90px;
    line-height: 79px;
    letter-spacing: -1.5px;
  }
  .subheadline {
    position: absolute;
    left: 62px;
    top: 328px;
    margin: 0;
    font-weight: 300;
    font-size: 33px;
    line-height: 47px;
    letter-spacing: -0.3px;
  }
  .monogram {
    position: absolute;
    right: 56px;
    top: 262px;
    margin: 0;
    font-weight: 600;
    font-size: 176px;
    line-height: 1;
    letter-spacing: -4px;
  }
</style>
</head>
<body>
  <div class="banner">
    <div class="banner__texture" role="img" aria-label="Dark close-up photograph of cracked clear ice on black"></div>
    <h1 class="headline">Your business is<br>too valuable to be<br>run on hope.</h1>
    <p class="subheadline">You didn’t build a business<br>to become its prisoner.</p>
    <p class="monogram" aria-label="Paul Whitaker">PW</p>
  </div>
</body>
</html>
```